Album cover for electronic pop band

Electronic pop album.Name of album: DRILLING HOLES INTO THE SUN1. I have included the first album cover we did. I would like to keep the logo the same.2. Included the logo and main picture file.3. I thought it would be cool to do a futuristic cover inversion/ negative look of the picture.

Serif

```html
<!DOCTYPE html>
<html lang="en">
<head>
<meta charset="utf-8">
<title>Folding Ladders Under a River — Album Cover</title>
<link rel="stylesheet" href="https://fonts.googleapis.com/css2?family=Orbitron:wght@600;700&display=swap">
<style>
  :root {
    --night: #17262a;
    --night-deep: #0f1b1f;
    --ice: #d6fbff;
    --mint: #b8efec;
    --teal: #3fa7a8;
    --cream: #eef4f2;
    --sun: #f6b43a;
    --ember: #ee6a2c;
    --magenta: #d7399a;
    --violet: #5a3bd0;
  }
  * { margin: 0; padding: 0; box-sizing: border-box; }
  html, body {
    width: 1200px;
    height: 1200px;
    overflow: hidden;
    background: var(--night);
  }
  .cover {
    position: relative;
    width: 1200px;
    height: 1200px;
    overflow: hidden;
    background:
      radial-gradient(ellipse at 70% 30%, #1f3236 0%, transparent 60%),
      linear-gradient(180deg, var(--night) 0%, var(--night) 80%, var(--night-deep) 100%);
  }
  .album-title {
    position: absolute;
    top: 60px;
    left: 0;
    width: 1200px;
    text-align: center;
    white-space: nowrap;
    font-family: "Orbitron", sans-serif;
    font-weight: 700;
    font-size: 35px;
    line-height: 44px;
    letter-spacing: 0.17em;
    padding-left: 0.17em;
    color: var(--ice);
  }
  .artwork {
    position: absolute;
    left: 0;
    top: 180px;
    width: 1160px;
    height: 900px;
    clip-path: polygon(0% 6%, 18% 2%, 40% 0%, 62% 4%, 78% 14%, 88% 30%, 96% 50%, 100% 72%, 96% 92%, 80% 100%, 0% 100%);
    background:
      radial-gradient(ellipse at 22% 20%, rgba(255,255,255,0.85) 0%, transparent 40%),
      radial-gradient(ellipse at 58% 32%, rgba(246,180,58,0.9) 0%, transparent 35%),
      radial-gradient(ellipse at 70% 55%, rgba(238,106,44,0.85) 0%, transparent 32%),
      radial-gradient(ellipse at 82% 78%, rgba(215,57,154,0.85) 0%, transparent 30%),
      radial-gradient(ellipse at 76% 62%, rgba(90,59,208,0.8) 0%, transparent 35%),
      radial-gradient(ellipse at 35% 55%, rgba(63,167,168,0.9) 0%, transparent 45%),
      linear-gradient(135deg, var(--cream) 0%, var(--mint) 35%, var(--teal) 70%, var(--night) 100%);
  }
  .artist-mark {
    position: absolute;
    right: 60px;
    top: 1082px;
    display: flex;
    align-items: center;
    gap: 16px;
  }
  .artist-mark__square {
    width: 16px;
    height: 16px;
    background: var(--mint);
  }
  .artist-mark__name {
    font-family: "Orbitron", sans-serif;
    font-weight: 700;
    font-size: 40px;
    line-height: 52px;
    color: var(--mint);
    letter-spacing: 0.02em;
    white-space: nowrap;
  }
</style>
</head>
<body>
  <main class="cover">
    <h1 class="album-title">FOLDING LADDERS UNDER A RIVER</h1>
    <div class="artwork" role="img" aria-label="Inverted negative-style photo of two figures standing back to back, surrounded by a burst of white, yellow, orange, magenta and violet paint with floating confetti shards"></div>
    <div class="artist-mark">
      <span class="artist-mark__square"></span>
      <span class="artist-mark__name">Lantern Foxes</span>
    </div>
  </main>
</body>
</html>
```